依頼詳細
栃木県の幹線道路50号線に2ヵ所野立て看板のデザインをお願いします。
参考デザインはあります。
車の通行量が1日2万台通りますので、一目でとんかつ屋があることを伝いたいです。

資料写真はあります。
少女系アニメキャラクターを入れた看板なんかも目を引いて面白いと思います。
記載項目
こだわりとんかつ朧月
新潟タレかつ丼!
特選から揚げ!
ご飯・キャベツ・味噌汁お代わり無料
150m先左
お持ち帰り弁当・宅配もやってます。
看板サイズH1800×W900

こだわりとんかつ朧月
新潟タレかつ丼
特選から揚げ
ご飯・キャベツ・味噌汁お代わり無料
直進2Km先右側
看板サイズH2400×W2700
希望イメージ
シンプル 複雑
単色 カラフル
暗い 明るい
日常 高級
遊び心 厳粛
未来的 伝統的
女性的 男性的
希望する色
黄・オレンジ系
納品ファイル
補足説明
■ 選んだ理由

当店のイメージに合ってました。

■ 提案者全員のお礼・コメント

今回は、ご提案頂きましてありがとうございました。
どの提案もとてもよかったです。大変迷いましたが決めさせていただきました。
次の機会もお願いいたします。

```html
<!DOCTYPE html>
<html lang="ja">
<head>
<meta charset="utf-8">
<title>こだわりとんかつ朧月 野立て看板</title>
<link href="https://fonts.googleapis.com/css2?family=Noto+Sans+JP:wght@900&family=Shippori+Mincho+B1:wght@800&family=Yuji+Boku&display=swap" rel="stylesheet">
<style>
  :root {
    --maroon: #5a1410;
    --maroon-deep: #3a0b08;
    --frame-red: #b11b16;
    --type-red: #c8161d;
    --cream: #f3ead6;
    --cream-dark: #e6d7b8;
    --ink: #111;
    --white: #fff;
    --yellow: #ffd21f;
    --band-yellow: #ffe56a;
  }
  * { margin: 0; padding: 0; box-sizing: border-box; }
  html, body { width: 1200px; height: 2396px; overflow: hidden; background: var(--maroon); }
  .billboard { position: relative; width: 1200px; height: 2396px; background: var(--maroon); overflow: hidden; }

  .direction-bar {
    position: absolute; left: 20px; top: 14px; width: 1160px; height: 270px;
    background: var(--white); border: 6px solid var(--frame-red);
    display: flex; align-items: center;
  }
  .direction-bar svg { margin-left: 30px; flex: none; }
  .direction-text {
    margin-left: 34px;
    font-family: "Noto Sans JP", sans-serif; font-weight: 900;
    font-size: 186px; line-height: 1; color: var(--ink); letter-spacing: -4px;
  }

  .main-panel {
    position: absolute; left: 24px; top: 300px; width: 1152px; height: 1520px;
    background: linear-gradient(180deg, var(--cream) 0%, var(--cream-dark) 100%);
    border: 8px solid var(--frame-red);
    overflow: hidden;
  }
  .free-refill {
    position: absolute; left: 80px; top: 60px;
    font-family: "Noto Sans JP", sans-serif; font-weight: 900;
    font-size: 100px; line-height: 1.2; color: var(--type-red);
  }
  .headline {
    position: absolute; right: 40px; top: 40px; height: 1440px;
    writing-mode: vertical-rl;
    font-family: "Yuji Boku", serif; font-size: 350px; line-height: 1;
    color: var(--ink);
    -webkit-text-stroke: 26px var(--white); paint-order: stroke fill;
    letter-spacing: 8px;
  }
  .dish-photo {
    position: absolute; left: 40px; top: 640px; width: 740px; height: 840px;
    border-radius: 48% 48% 46% 46%;
    background: radial-gradient(ellipse at 50% 38%, #d98a3a 0%, #b5601f 38%, #6b2f12 70%, #2a120a 100%);
  }
  .signature-badge {
    position: absolute; left: 60px; top: 480px; width: 680px; height: 220px;
    background: var(--maroon-deep); border: 5px solid var(--yellow);
    transform: rotate(-5deg);
    font-family: "Yuji Boku", serif; color: var(--yellow);
    padding: 16px 30px;
    white-space: nowrap;
  }
  .signature-badge .badge-sub { display: block; font-size: 60px; line-height: 1.1; }
  .signature-badge .badge-main { display: block; font-size: 100px; line-height: 1.15; }

  .karaage-line {
    position: absolute; left: 24px; top: 1830px; width: 1152px; height: 130px;
    background: var(--cream);
    display: flex; align-items: center; justify-content: center;
    font-family: "Shippori Mincho B1", serif; font-weight: 800;
    font-size: 80px; color: var(--ink);
  }
  .takeout-line {
    position: absolute; left: 24px; top: 1968px; width: 1152px; height: 122px;
    background: var(--band-yellow);
    display: flex; align-items: center; justify-content: center;
    font-family: "Noto Sans JP", sans-serif; font-weight: 900;
    font-size: 68px; color: var(--type-red);
  }
  .store-footer {
    position: absolute; left: 0; top: 2100px; width: 1200px; height: 296px;
    background: var(--maroon-deep);
    display: flex; align-items: center; justify-content: center; gap: 50px;
  }
  .store-name {
    font-family: "Shippori Mincho B1", serif; font-weight: 800;
    font-size: 86px; color: var(--white);
  }
  .store-square {
    width: 150px; height: 150px; background: var(--frame-red); flex: none;
  }
</style>
</head>
<body>
<div class="billboard">
  <header class="direction-bar">
    <svg width="190" height="190" viewBox="0 0 190 190" aria-hidden="true">
      <circle cx="95" cy="95" r="92" fill="#ffd21f"/>
      <path d="M120 150 V80 H75" fill="none" stroke="#c8161d" stroke-width="26"/>
      <polygon points="40,80 85,45 85,115" fill="#c8161d"/>
    </svg>
    <span class="direction-text">150m先左</span>
  </header>

  <section class="main-panel">
    <p class="free-refill">ご飯・味噌汁<br>キャベツ・<br>おかわり無料</p>
    <div class="dish-photo" role="img" aria-label="新潟タレかつ丼の写真"></div>
    <div class="signature-badge">
      <span class="badge-sub">名物! 新潟</span>
      <span class="badge-main">タレかつ丼!</span>
    </div>
    <h1 class="headline">とんかつ</h1>
  </section>

  <p class="karaage-line">自慢の特選から揚げもどうぞ!</p>
  <p class="takeout-line">お持ち帰り弁当・宅配もやってます</p>

  <footer class="store-footer">
    <span class="store-name">こだわりとんかつ朧月</span>
    <span class="store-square" aria-hidden="true"></span>
  </footer>
</div>
</body>
</html>
```